Telecommunications/Power civil contractor needs business card design

Were a new telecommunications/power underground civil contractor that is looking for a new business card design. Our company colours are silver or grey and orange. Feel free to use the white background logo or the black background logo.

Target Market(s)

Local contractors, utility companies, private sector mining/energy companies, developers.

Industry/Entity Type

Telecommunications

Contact Information for Business Card

Each card will need the following info:
Persons name:
Title:
E-mail:
Phone number:
Shop Address:
Mailing Address:

Requirements
Must have
• Each card will need the following info:
• Persons name:
• Title:
• E-mail:
• Phone number:
• Shop Address:
• Mailing Address:

```html
<!DOCTYPE html>
<html lang="en">
<head>
<meta charset="utf-8">
<title>Trenchline Contracting Inc – Business Card</title>
<link href="https://fonts.googleapis.com/css2?family=Arimo:wght@400;700&display=swap" rel="stylesheet">
<style>
  :root {
    --stage: #2b2b2b;
    --card-dark: #1c1c1c;
    --card-dark-2: #343434;
    --card-light: #f4f4f4;
    --card-light-2: #dcdcdc;
    --orange: #e2561f;
    --ink: #1e1e1e;
    --grey-ink: #4a4a4a;
    --silver: #9a9a9a;
  }
  * { margin: 0; padding: 0; box-sizing: border-box; }
  html, body {
    width: 1200px;
    height: 997px;
    overflow: hidden;
    background: var(--stage);
    font-family: "Arimo", Arial, sans-serif;
  }
  .stage {
    position: relative;
    width: 1200px;
    height: 997px;
    display: flex;
    align-items: center;
    justify-content: center;
  }
  .business-card {
    position: relative;
    width: 840px;
    height: 480px;
    border-radius: 26px;
    overflow: hidden;
    display: flex;
    box-shadow: 0 18px 40px rgba(0,0,0,0.55);
  }
  .brand-panel {
    position: relative;
    width: 340px;
    height: 100%;
    background: linear-gradient(150deg, var(--card-dark-2) 0%, var(--card-dark) 55%, #262626 100%);
    display: flex;
    align-items: center;
    justify-content: center;
  }
  .brand-panel .pattern {
    position: absolute;
    inset: 0;
    background: linear-gradient(135deg, rgba(255,255,255,0.05), rgba(0,0,0,0.15));
  }
  .brand-lockup {
    position: relative;
    display: flex;
    flex-direction: column;
    align-items: center;
    gap: 18px;
  }
  .brand-mark {
    width: 110px;
    height: 110px;
    border-radius: 50%;
    border: 6px solid var(--silver);
  }
  .brand-name {
    color: var(--orange);
    font-weight: 700;
    font-size: 30px;
    line-height: 1.1;
    text-align: center;
    letter-spacing: 1px;
    text-transform: uppercase;
  }
  .details-panel {
    flex: 1;
    height: 100%;
    background: linear-gradient(160deg, var(--card-light) 0%, #ffffff 40%, var(--card-light-2) 100%);
    padding: 52px 56px 0 0;
    display: flex;
    flex-direction: column;
    align-items: flex-end;
    text-align: right;
  }
  .entry {
    position: relative;
    padding-right: 16px;
  }
  .entry::after {
    content: "";
    position: absolute;
    right: 0;
    top: 2px;
    width: 4px;
    height: 24px;
    background: var(--orange);
  }
  .person-name {
    font-weight: 700;
    font-size: 21px;
    color: var(--grey-ink);
  }
  .person-title {
    font-size: 16px;
    color: var(--orange);
  }
  .divider {
    width: 300px;
    height: 1px;
    background: var(--ink);
    margin: 18px 0 0 0;
    align-self: flex-end;
  }
  .label {
    font-size: 18px;
    color: var(--orange);
  }
  .value {
    font-size: 18px;
    color: var(--ink);
    margin-top: 2px;
  }
  .contact-list {
    margin-top: 10px;
    display: flex;
    flex-direction: column;
    align-items: flex-end;
    gap: 22px;
  }
</style>
</head>
<body>
  <main class="stage">
    <article class="business-card">
      <section class="brand-panel">
        <div class="pattern" role="img" aria-label="Dark grey geometric triangle pattern background"></div>
        <div class="brand-lockup">
          <div class="brand-mark"></div>
          <div class="brand-name">Trenchline<br>Contracting Inc</div>
        </div>
      </section>
      <section class="details-panel">
        <div class="entry">
          <div class="person-name">Daniel Hartley</div>
          <div class="person-title">Chairman</div>
        </div>
        <div class="divider"></div>
        <div class="contact-list">
          <div class="entry">
            <div class="label">Phone</div>
            <div class="value">0400123456</div>
          </div>
          <div class="entry">
            <div class="label">Email</div>
            <div class="value">care@trenchlinecontracting.com</div>
          </div>
          <div class="entry">
            <div class="label">Shop Address</div>
            <div class="value">shop no 9, near park, Ashford</div>
          </div>
          <div class="entry">
            <div class="label">Mailing Address</div>
            <div class="value">Rd. mill market, Ashford</div>
          </div>
        </div>
      </section>
    </article>
  </main>
</body>
</html>
```